VELKORIS Stationery Design Project

I want a stationery design for a web development company consists of:
1- business card
2- Letter Head
3- small Envelope
4- Large Envelope

need a very clean professional simple design yet creative,

The company logo is attached
http://www.pixelbazaarhub.net/project-progress/designs.aspx?briefId=5830174&submissionId=47210938

logo font is sui generis rg (attached)
I would like to have the stationery text font to be helvetica font regular or light (can be changed)

I love the combination of cyan, black and grey colors
( will attach some recommended styles)

Business

• curves or waves

```html
<!DOCTYPE html>
<html lang="en">
<head>
<meta charset="utf-8">
<title>VELKORIS Stationery</title>
<link rel="stylesheet" href="https://fonts.googleapis.com/css2?family=Inter:wght@300;400;600&display=swap">
<style>
  :root {
    --cyan: #1fa3dc;
    --black: #0a0a0a;
    --charcoal: #242424;
    --grey: #8a8a8a;
    --light-grey: #e2e2e2;
    --paper: #ffffff;
    --backdrop: #eceeef;
    --body-text: #2a2a2a;
  }
  * { box-sizing: border-box; margin: 0; padding: 0; }
  html, body { width: 1200px; height: 900px; overflow: hidden; }
  body {
    background: var(--backdrop);
    font-family: "Inter", "Helvetica Neue", Arial, sans-serif;
    font-weight: 300;
    position: relative;
  }
  .piece { position: absolute; box-shadow: 0 2px 8px rgba(0,0,0,.12); overflow: hidden; }

  .brand {
    display: flex; align-items: center; gap: 6px;
    color: var(--cyan); font-weight: 400; letter-spacing: .22em;
  }
  .brand-square { width: 8px; height: 8px; background: var(--cyan); flex: none; }

  /* Small envelope, back view */
  .envelope-small { left: 40px; top: 40px; width: 420px; height: 210px; background: var(--paper); }
  .envelope-small svg { position: absolute; inset: 0; }

  /* Business cards */
  .card { top: 290px; width: 204px; height: 118px; }
  .card-front { left: 40px; background: var(--charcoal); display: flex; align-items: center; justify-content: center; }
  .card-front .brand { font-size: 13px; }
  .card-back { left: 256px; background: var(--paper); }
  .card-back .brand { font-size: 10px; position: absolute; left: 14px; top: 48px; }
  .card-back .brand-square { width: 6px; height: 6px; }
  .card-person { position: absolute; right: 14px; top: 16px; text-align: right; }
  .card-name { font-size: 8px; color: var(--body-text); font-weight: 400; }
  .card-role { font-size: 6px; color: var(--grey); margin-top: 2px; }
  .card-contact {
    position: absolute; left: 108px; top: 56px; width: 90px;
    font-size: 5.5px; line-height: 1.6; color: var(--body-text); white-space: nowrap;
  }

  /* Large envelope */
  .envelope-large { left: 40px; top: 440px; width: 440px; height: 311px; background: var(--black); }
  .envelope-large .brand { position: absolute; left: 26px; top: 30px; font-size: 13px; }
  .envelope-footer { position: absolute; left: 26px; bottom: 20px; font-size: 6px; line-height: 1.6; color: var(--paper); }

  /* Letterheads */
  .letterhead { top: 224px; width: 320px; height: 452px; }
  .letterhead-dark { left: 510px; background: var(--charcoal); }
  .letterhead-light { left: 850px; background: var(--paper); }
  .letterhead .brand { position: absolute; left: 24px; top: 30px; font-size: 12px; }
  .letter-body {
    position: absolute; left: 52px; right: 24px; top: 92px;
    font-size: 5.2px; line-height: 1.5; color: var(--body-text); font-weight: 400; text-align: justify;
  }
  .letter-body p { margin-bottom: 6px; }
  .signature { display: block; margin-top: 4px; }
  .letter-footer {
    position: absolute; left: 24px; right: 24px; bottom: 22px;
    display: flex; gap: 14px; font-size: 5.5px; letter-spacing: .04em; white-space: nowrap;
  }
  .letterhead-dark .letter-footer { color: var(--paper); }
  .letterhead-light .letter-footer { color: var(--body-text); }
  .letter-footer .label { color: var(--grey); margin-right: 3px; }
</style>
</head>
<body>

  <div class="piece envelope-small">
    <svg width="420" height="210" viewBox="0 0 420 210" aria-hidden="true">
      <polygon points="0,0 420,0 420,58 0,58" fill="var(--charcoal)"/>
      <polygon points="14,58 406,58 370,100 50,100" fill="var(--light-grey)"/>
    </svg>
  </div>

  <div class="piece card card-front">
    <div class="brand"><span class="brand-square"></span>VELKORIS</div>
  </div>

  <div class="piece card card-back">
    <div class="brand"><span class="brand-square"></span>VELKORIS</div>
    <div class="card-person">
      <div class="card-name">Daniel Brenner</div>
      <div class="card-role">Manager</div>
    </div>
    <div class="card-contact">
      12 Harbor Lane, Portview<br>
      Tel : 0147 58203961<br>
      Fax : 0147 58203962<br>
      web : www.velkoris.net<br>
      email : hello@velkoris.net
    </div>
  </div>

  <div class="piece envelope-large">
    <div class="brand"><span class="brand-square"></span>VELKORIS</div>
    <div class="envelope-footer">Tel : 0147 58203961<br>web : www.velkoris.net</div>
  </div>

  <div class="piece letterhead letterhead-dark">
    <div class="brand"><span class="brand-square"></span>VELKORIS</div>
    <div class="letter-footer">
      <span><span class="label">email :</span>hello@velkoris.net</span>
      <span><span class="label">Tel :</span>0147 58203961</span>
      <span><span class="label">web :</span>www.velkoris.net</span>
    </div>
  </div>

  <div class="piece letterhead letterhead-light">
    <div class="brand"><span class="brand-square"></span>VELKORIS</div>
    <div class="letter-body">
      <p>Thank you for choosing our studio for your next web project. Our team builds fast, accessible and carefully crafted websites that help growing businesses reach new customers online. Every project begins with a short discovery phase, where we learn about your goals, your audience and the tone you want your brand to carry. From there we shape a clear plan covering structure, design, development and launch, so that each step is visible and easy to follow. We keep communication simple and regular, sharing progress in small steps and inviting your feedback at every stage of the work.</p>
      <p>Enclosed you will find a summary of the proposed scope, an outline of the timeline and an estimate of the costs involved. Please review these documents at your convenience and let us know if any detail should be adjusted before we begin.</p>
      <p>We look forward to working with you and to building a website that reflects the quality of your business. Should you have any questions, our project team is always happy to help by phone or by email during regular office hours.</p>
      <svg class="signature" width="60" height="14" role="img" aria-label="Handwritten signature of Daniel Brenner">
        <rect width="60" height="14" fill="var(--light-grey)"/>
      </svg>
    </div>
    <div class="letter-footer">
      <span><span class="label">email :</span>hello@velkoris.net</span>
      <span><span class="label">Tel :</span>0147 58203961</span>
      <span><span class="label">web :</span>www.velkoris.net</span>
    </div>
  </div>

</body>
</html>
```